Customs House descriptive business cards

We require a two-sided business card that has a simple yet elegant design. We want to be able to promote our services as a customs house. This card should include our logo, contact info and services offered with the logo being on one side and the contact info and services on the flip side

Target Market(s)

Importers / exporters to and from the Bahamas

Industry/Entity Type

Logistics

Contact Information for Business Card

The front side of the card could have the logo and the flip side should have the other relevant info

Font styles to use
Serif

Colors

Designer to choose colors to be used in the design.

Requirements
Must have
• (Harbourline Agents Ltd) Logo, address and contact info also services:
• import customs clearance, Delivery & HAndling services,Florida pickups, Export packing & Crating Services, export customs clearance, Consulting

```html
<!DOCTYPE html>
<html lang="en">
<head>
<meta charset="utf-8">
<title>Harbourline Agents Ltd — Business Card</title>
<link rel="stylesheet" href="https://fonts.googleapis.com/css2?family=Lora:ital,wght@0,400;0,600;0,700;1,400;1,600&display=swap">
<style>
  :root {
    --bg: #e9e6e1;
    --card-white: #f7f7f7;
    --brand-blue: #1f8fd0;
    --deep-blue: #1466b3;
    --light-blue: #2aa8dc;
    --text-grey: #8a8a8a;
    --rule-grey: #cfcfcf;
    --white: #ffffff;
  }
  html, body {
    margin: 0;
    padding: 0;
    width: 1200px;
    height: 780px;
    overflow: hidden;
    background: var(--bg);
    font-family: "Lora", Georgia, serif;
  }
  .canvas {
    position: relative;
    width: 1200px;
    height: 780px;
  }

  /* Front: contact side */
  .card-front {
    position: absolute;
    left: 90px;
    top: 80px;
    width: 380px;
    height: 620px;
    background: var(--card-white);
    border-radius: 22px;
    box-shadow: 0 10px 28px rgba(0,0,0,.18);
    overflow: hidden;
    text-align: center;
    color: var(--text-grey);
  }
  .brand-name {
    margin: 80px 0 0;
    font-size: 27px;
    font-weight: 600;
    color: var(--brand-blue);
    letter-spacing: .5px;
  }
  .brand-rule {
    width: 250px;
    height: 1px;
    background: var(--rule-grey);
    margin: 14px auto 26px;
  }
  .person-name {
    margin: 0;
    font-size: 24px;
    font-weight: 700;
    color: var(--brand-blue);
    text-transform: uppercase;
    letter-spacing: .5px;
  }
  .person-title {
    margin: 4px 0 0;
    font-size: 17px;
    color: var(--text-grey);
  }
  .contact-list {
    margin: 24px auto 0;
    width: 300px;
    padding: 0;
    list-style: none;
  }
  .contact-item {
    border-top: 1px solid var(--rule-grey);
    padding: 9px 0 7px;
    font-size: 16px;
  }
  .contact-label {
    display: block;
    font-size: 13px;
    font-style: italic;
    font-weight: 600;
    color: var(--brand-blue);
  }
  .address {
    border-top: 1px solid var(--rule-grey);
    width: 300px;
    margin: 0 auto;
    padding-top: 10px;
    font-size: 15px;
    line-height: 1.35;
  }
  .front-band {
    position: absolute;
    left: 0;
    right: 0;
    bottom: 0;
    height: 64px;
    background: linear-gradient(90deg, var(--deep-blue), var(--light-blue));
    color: var(--white);
    font-size: 19px;
    letter-spacing: 2px;
    line-height: 64px;
  }

  /* Back: brand & services side */
  .card-back {
    position: absolute;
    left: 520px;
    top: 200px;
    width: 610px;
    height: 380px;
    border-radius: 22px;
    box-shadow: 0 10px 28px rgba(0,0,0,.22);
    overflow: hidden;
    color: var(--white);
  }
  .back-texture {
    position: absolute;
    inset: 0;
    background: radial-gradient(ellipse at 80% 10%, var(--light-blue), var(--deep-blue) 75%);
  }
  .back-content {
    position: relative;
    padding: 70px 50px 0;
  }
  .back-brand {
    margin: 0;
    font-size: 40px;
    font-weight: 600;
    text-align: center;
    letter-spacing: 1px;
  }
  .back-rule {
    width: 440px;
    height: 2px;
    background: var(--white);
    margin: 18px auto 0;
    opacity: .9;
  }
  .services {
    position: absolute;
    left: 34px;
    right: 34px;
    top: 290px;
    font-size: 15px;
    line-height: 1.5;
    text-align: left;
  }
  .services p { margin: 0; }
</style>
</head>
<body>
<main class="canvas">

  <section class="card-front" aria-label="Contact side">
    <h1 class="brand-name">Harbourline Agents Ltd</h1>
    <div class="brand-rule"></div>
    <h2 class="person-name">Marcus Dellwood</h2>
    <p class="person-title">Operations Director</p>
    <ul class="contact-list">
      <li class="contact-item"><span class="contact-label">Cell:</span>(242) 555-0142</li>
      <li class="contact-item"><span class="contact-label">Office:</span>(242) 555-0178</li>
      <li class="contact-item"><span class="contact-label">Email:</span>imports@harbourlineagents.com</li>
    </ul>
    <p class="address">#42 Palmetto Lane<br>P.O. BOX SP-50217, Nassau<br>Bahamas</p>
    <div class="front-band">www.harbourlineagents.com</div>
  </section>

  <section class="card-back" aria-label="Brand and services side">
    <div class="back-texture" role="img" aria-label="Faint repeating decorative pattern over blue gradient"></div>
    <div class="back-content">
      <h2 class="back-brand">Harbourline Agents Ltd.</h2>
      <div class="back-rule"></div>
    </div>
    <div class="services">
      <p>import customs clearance | Delivery &amp; HAndling services | Florida pickups</p>
      <p>Export packing &amp; Crating Services | export customs clearance | Consulting</p>
    </div>
  </section>

</main>
</body>
</html>
```